PLN Info Brochure

We need a brochure design for a new not-for-profit organisation that is aimed at providing homeless people with a residence that also provides counselling and vocational training to assist them to find suitable employment at the end of the program.
PLEASE NOTE:
Brochure to be A4.
I know the brochure is quite long, it is really a booklet, but please note that it does not have to have a lot of work done on it, I just want it to look professional and the front cover and inside page to look good.
Also please leave about 2-3 pages at the end as I will be adding in some architect drawings.
Please add in a last page with Contact written at the bottom - we will fill that in later. So please ensure it is editable in PDF.
Thank you so much.
Cheers
Nadine
Training

```html
<!DOCTYPE html>
<html lang="en">
<head>
<meta charset="utf-8">
<title>PLN Info Brochure – Spread</title>
<link rel="stylesheet" href="https://fonts.googleapis.com/css2?family=Cutive&family=Open+Sans:wght@400;600;700&display=swap">
<style>
  :root {
    --backdrop: #2a2a2a;
    --paper: #ffffff;
    --paper-shade: #eeeeee;
    --accent: #f0a31c;
    --ink: #222222;
    --ink-soft: #555555;
    --rule: #e3a53a;
  }
  * { box-sizing: border-box; margin: 0; padding: 0; }
  html, body { width: 1200px; height: 861px; overflow: hidden; }
  body { background: var(--backdrop); font-family: "Open Sans", Arial, sans-serif; color: var(--ink); position: relative; }

  .spread { position: absolute; left: 60px; top: 50px; width: 1080px; height: 760px; display: flex; box-shadow: 0 10px 30px rgba(0,0,0,.5); }
  .page { position: relative; width: 540px; height: 760px; background: var(--paper); overflow: hidden; }
  .page--left { background: linear-gradient(to right, var(--paper) 88%, var(--paper-shade)); }
  .page--right { background: linear-gradient(to left, var(--paper) 90%, var(--paper-shade)); }

  .page-tab { position: absolute; top: 0; width: 30px; height: 30px; background: var(--accent); color: #fff; font-size: 8px; font-weight: 700; display: flex; align-items: flex-end; justify-content: center; padding-bottom: 4px; }
  .page--left .page-tab { left: 50px; }
  .page--right .page-tab { right: 50px; }

  .section-title { position: absolute; font-family: "Cutive", "Courier New", serif; color: var(--accent); font-size: 30px; font-weight: 400; }
  .page--left .section-title { left: 52px; top: 50px; }
  .page--right .section-title { left: 40px; top: 50px; }

  .photo { position: absolute; }
  .photo--street { left: 30px; top: 108px; width: 205px; height: 440px; background: linear-gradient(160deg, #5a4a3e 0%, #8a6d55 35%, #6f6a64 65%, #b9b2a6 100%); }
  .photo--meal { left: 40px; top: 180px; width: 325px; height: 210px; background: linear-gradient(135deg, #3c2e2a 0%, #7a5c6e 40%, #c9b9c9 60%, #4b3a33 100%); }

  .facts { position: absolute; left: 250px; top: 112px; width: 265px; font-size: 7.4px; line-height: 10.2px; font-weight: 600; }
  .facts p { margin-bottom: 1px; }
  .facts ul { list-style: none; }
  .facts li { padding-left: 9px; position: relative; }
  .facts li::before { content: ""; position: absolute; left: 1px; top: 3.5px; width: 4px; height: 4px; background: var(--accent); }
  .facts .note { color: #6a6a6a; }

  .sources { position: absolute; left: 30px; top: 604px; width: 440px; font-size: 6.2px; line-height: 8.5px; color: var(--ink-soft); }

  .intro { position: absolute; left: 40px; top: 100px; width: 450px; font-size: 6.8px; line-height: 9.2px; color: var(--ink-soft); }
  .intro p + p { margin-top: 4px; }

  .subsection { position: absolute; top: 412px; width: 195px; }
  .subsection--physio { left: 40px; }
  .subsection--psych { left: 275px; }
  .subsection h3 { font-family: "Cutive", "Courier New", serif; color: var(--accent); font-size: 17px; font-weight: 400; margin-bottom: 10px; }
  .subsection p { font-size: 6.6px; line-height: 9.2px; color: var(--ink-soft); }
  .subsection p + p { margin-top: 4px; }
  .divider { position: absolute; left: 255px; top: 410px; width: 1px; height: 230px; background: var(--rule); }
  .divider-top { position: absolute; left: 255px; top: 410px; width: 215px; height: 1px; background: var(--rule); }
</style>
</head>
<body>
  <main class="spread">
    <section class="page page--left">
      <div class="page-tab">02</div>
      <h1 class="section-title">1. Homeless</h1>
      <div class="photo photo--street" role="img" aria-label="Photograph of a man sitting on a city footpath in a sleeping bag beside a hand-written cardboard sign"></div>
      <div class="facts">
        <p>Numerous national, state and local reports repeatedly indicate that there is not one single cause that leads to homelessness. However, without the financial ability to make ends meet and afford a home, individuals and families become homeless. Other factors that contribute to homelessness include:</p>
        <ul>
          <li>Poverty</li>
          <li>Unemployment</li>
          <li>Lack of affordable housing</li>
          <li>Poor physical or mental health</li>
          <li>Drug and alcohol abuse</li>
          <li>Gambling</li>
          <li>Family and relationship breakdown</li>
          <li>Domestic violence</li>
          <li>Physical and/or sexual abuse</li>
        </ul>
        <p>There are currently 105,237 people in Australia who are homeless. The rate of homelessness is 49 out of every 10,000 people (0.5% of the population). There are approximately 56% male and 44% female. The age breakdown is as follows;</p>
        <ul>
          <li>Under 12 17% (17,845)</li>
          <li>12–18 10% (10,913)</li>
          <li>19–24 15% (15,325)</li>
          <li>25–34 18% (19,312)</li>
          <li>35–44 14% (14,484)</li>
          <li>45–54 12% (12,507)</li>
          <li>55–64 8% (8,649)</li>
          <li>65–74 4% (4,174)</li>
          <li>75 and over 2% (2,028)</li>
        </ul>
        <p>Due to the wide spread of demographics of homeless people, PLN will cater for all age ranges and sexes, as well as family groups. The target market for PLN will be anyone that is homeless, ‘sleeping rough’ or ‘couch surfing’. Secondary placement consideration will also be given to anyone else on a case-by-case basis. The current homeless statistics are as follows;</p>
        <ul>
          <li>NSW 28,190 (40.8 people per 10,000)</li>
          <li>VIC 22,789 (42.6 people per 10,000)</li>
          <li>QLD 19,838 (48.5 people per 10,000)</li>
          <li>SA 5,985 (37.5 people per 10,000)</li>
          <li>WA 9,592 (42.8 people per 10,000)</li>
          <li>TAS 1,579 (31.9 people per 10,000)</li>
          <li>NT 15,479 (730.7 people per 10,000)</li>
          <li>ACT 1,785 (50 people per 10,000)</li>
        </ul>
      </div>
      <div class="sources">
        <p>http://www.reliefcircle.org.au/en/Who-We-Are/our-work/Homelessness/Why-are-people-homeless/default.html</p>
        <p>http://www.shelternetwork.org.au/index.php/about-homelessness/homeless-statistics</p>
        <p>the practice of sleeping overnight in the houses of friends or fellow members of a social network, esp. as an alternative to staying in hotels, hostels, etc (Harlow Dictionary online)</p>
      </div>
    </section>

    <section class="page page--right">
      <div class="page-tab">03</div>
      <h2 class="section-title">2. Program Overview</h2>
      <div class="intro">
        <p>PLN Legacy Foundation (PLN) aims to provide homeless people (Residents) with the tools necessary to re-enter society as functional, productive and balanced members of society. PLN aims to assist homeless people, not by just giving them a shelter, but by addressing the initial cause of homelessness and provide the tools necessary to gain independent living, in an aim to stop the cycle.</p>
        <p>PLN will house Residents in a residential facility, while they are at the facility they will receive physiological and psychological care, assistance with basic society/life skills and/or vocational skills and training. Once the Residents have completed their program, PLN will assist them to fit back into society, find a job (if relevant), appropriate housing, schooling etc. PLN will continue to provide Residents with Outreach and After Care assistance for as long as required.</p>
      </div>
      <div class="photo photo--meal" role="img" aria-label="Photograph of people sharing a meal at a long table decorated with purple flowers"></div>

      <div class="divider-top"></div>
      <div class="divider"></div>

      <article class="subsection subsection--physio">
        <h3>2.1 Physiological</h3>
        <p>Due to poor diet, malnutrition and exposure, homeless people are at greater risk of suffering from chronic health disorders like asthma, hepatitis and diabetes. Furthermore, many homeless adolescents find that exchanging sex for food, clothing and shelter is their only means of survival on the streets. Reportedly one in three youths have traded sex for survival, which means they are at greater risk of contracting AIDS, HIV-related illnesses and other STDs.</p>
        <p>In addition, older homeless people may suffer significant health and psychological disorders that go untreated for long periods of time. As part of the initial intake process, PLN will do a complete physical assessment of each Resident to assess their level of health. A program of treatment will be initiated in accordance with the results of the medical and dental assessment.</p>
      </article>

      <article class="subsection subsection--psych">
        <h3>2.2 Psychological</h3>
        <p>A majority of Residents will experience some form of anxiety disorders, depression, post-traumatic stress disorder and suicidal thoughts due to the increased exposure to violence while homeless. Therefore, it will be a requirement for all Residents to undertake counselling sessions throughout their day at a PLN facility.</p>
        <p>At the initial intake process a full psychological analysis will be undertaken and a specific program will be developed for each Resident. Regular counselling sessions (and any other treatment necessary) will be conducted to address each Residents issues with the aim of addressing the cause/impact of homelessness.</p>
      </article>
    </section>
  </main>
</body>
</html>
```